Ferncrest Dental, LLC business card project

Business card to be designed with current logo.
Dental office- please keep design of card that looks clean and professional.
Please include the following info:
Ferncrest Dental, LLC
Dr. Lorna Pettigrew
2871 Marlowe Street
Bethlehem, PA 18093
610-555-0193
ferncrestdental.office@examplemail.test
Hello everyone-
Reason: Just got back from overseas- will look at all designs and provide feedback. Thank you!
Reason: Polling my friends for the final selection-
thank you to all those that participated- so many talented designers!

```html
<!DOCTYPE html>
<html lang="en">
<head>
<meta charset="utf-8">
<title>Ferncrest Dental, LLC — Business Card</title>
<link rel="stylesheet" href="https://fonts.googleapis.com/css2?family=Roboto+Condensed:wght@400;700&display=swap">
<style>
  :root {
    --page-bg: #ffffff;
    --forest: #0f4200;
    --lime: #aaff00;
    --leaf: #8ee000;
    --ink: #0e3d00;
    --contact-ink: #111a05;
  }
  * { margin: 0; padding: 0; box-sizing: border-box; }
  html, body {
    width: 1200px;
    height: 676px;
    overflow: hidden;
    background: var(--page-bg);
  }
  .canvas {
    position: relative;
    width: 1200px;
    height: 676px;
    overflow: hidden;
    font-family: "Roboto Condensed", "Arial Narrow", sans-serif;
  }
  .card {
    position: absolute;
    left: 44px;
    top: 44px;
    width: 1099px;
    height: 640px;
    background: var(--lime);
  }
  .card-header {
    position: absolute;
    left: 0;
    top: 0;
    width: 100%;
    height: 278px;
    background: var(--forest);
    box-shadow: 0 8px 14px rgba(0, 0, 0, 0.45);
    display: flex;
    align-items: center;
    justify-content: center;
    gap: 22px;
  }
  .brand-dot {
    width: 46px;
    height: 46px;
    border-radius: 50%;
    background: var(--leaf);
    flex: none;
  }
  .brand-name {
    font-weight: 400;
    font-size: 76px;
    line-height: 1;
    color: var(--leaf);
    letter-spacing: 0.5px;
  }
  .doctor-name {
    position: absolute;
    left: 126px;
    top: 348px;
    font-weight: 700;
    font-size: 40px;
    line-height: 1;
    color: var(--ink);
  }
  .contact-list {
    position: absolute;
    left: 506px;
    top: 352px;
    list-style: none;
    font-weight: 400;
    font-size: 32px;
    line-height: 56px;
    color: var(--contact-ink);
  }
</style>
</head>
<body>
  <main class="canvas">
    <article class="card">
      <header class="card-header">
        <span class="brand-dot" aria-hidden="true"></span>
        <span class="brand-name">Ferncrest Dental, LLC</span>
      </header>
      <h1 class="doctor-name">Dr. Lorna Pettigrew</h1>
      <ul class="contact-list">
        <li>2871 Marlowe Street</li>
        <li>Bethlehem, PA 18093</li>
        <li>610.555.0193</li>
        <li>ferncrestdental.office@examplemail.test</li>
      </ul>
    </article>
  </main>
</body>
</html>
```